Junk Removal Website Design

We are working with a Junk Removal company in California. They provide junk hauling services for commercial and residential throughout California.
Some sites to use for inspiration:
https://www.clearbarrowhauls.com
https://pebblecartworkteam.com
https://www.fernwayliftersandmovers.com
https://www.mistoakcleanupcrew.com
Thank you for taking the time to consider designing a website for us. We are web developers based in Stockton, CA, USA. Most of our projects go through the same process. Understanding this process may help you win a project with us. We custom-code all of our websites in-house. We don’t have any requirements as to what tools you use for your design, but we ask that you follow these guidelines.
IMAGES:
If you use any images or icons in the design, we ask that you have a link to the asset so we can purchase the image/icon. Most of the designs we submit do not have the customer’s images on them unless they have some great images. Be creative; show us the feeling you are trying to portray with your image choices. Use any royalty-free site you choose. We subscribe to Vontrel and mainly use their images, but we can purchase images outside of Vontrel. PLEASE NOTE: we will not submit designs to clients with watermarks on the images.
FONTS:
We ask that you identify the fonts you’re using in the design. This can be done in a message if you want. We typically use Quimbly Fonts and Vontrel Fonts.
CONTENT:
We're always open to different content and ideas. We often submit designs with stock images so the client can see our vision. We typically take pictures after the website launch to use their images with our vision. Lorem Ipsum is fine for paragraphs, but we ask that you make the Headers with correct English. We want to be able to show the vision and identify the sections of the website.
INSPIRATION:
We typically add a couple of links in the brief of websites we like to help you get started in your design.
REVISIONS:
We do not often ask for revisions of the designs unless we see something in the design that may not appeal to the client. If there are slight changes that we want to make, we do that in the development process.
FEEDBACK:
We rarely give feedback on designs during the design process. We are working on many website projects and do not have the time to provide feedback. We usually respond if your request is well thought out and asks specific questions, but a note asking “feedback, please” usually goes unanswered.
Number of Pages Required
1 page

```html
<!DOCTYPE html>
<html lang="en">
<head>
<meta charset="utf-8">
<title>Haulwell – Junk Removal</title>
<link href="https://fonts.googleapis.com/css2?family=Roboto+Slab:wght@400;600;700&family=Montserrat:ital,wght@0,400;0,500;0,600;1,400&family=Oswald:wght@500&family=Roboto+Condensed:wght@700&display=swap" rel="stylesheet">
<style>
:root{
  --green:#53a843;
  --green-dark:#3f8a32;
  --green-light:#6cbf5b;
  --ink:#1f1f24;
  --dark:#242428;
  --text:#3a3a3a;
  --muted:#6b6b6b;
  --white:#ffffff;
  --star:#f5a623;
}
*{box-sizing:border-box;margin:0;padding:0}
html,body{width:1200px;height:4199px;overflow:hidden;background:var(--white)}
body{position:relative;font-family:"Montserrat",sans-serif;color:var(--text)}
.abs{position:absolute}
.slab{font-family:"Roboto Slab",serif}

/* header */
.topbar{left:305px;top:0;width:895px;height:36px;background:var(--green)}
.topbar-phone{right:22px;top:2px;display:flex;align-items:center;gap:8px;color:var(--ink)}
.topbar-phone small{font:600 12px "Roboto Slab",serif}
.topbar-phone strong{font:700 25px "Roboto Condensed",sans-serif}
.navbar{left:0;top:36px;width:1200px;height:70px;background:var(--white)}
.logo-box{left:111px;top:0;width:194px;height:142px;background:var(--white);border-radius:0 0 8px 8px;box-shadow:0 4px 14px rgba(0,0,0,.18);display:flex;align-items:center;justify-content:center;z-index:5}
.logo-name{font:700 34px "Roboto Slab",serif;color:var(--ink)}
.nav{left:360px;top:66px;display:flex;gap:34px;font:600 14px "Roboto Slab",serif;color:var(--ink)}
.nav .active{color:var(--green)}
.nav-sep{left:905px;top:60px;width:1px;height:28px;background:#999}
.search{left:918px;top:64px}
.btn-contact{left:949px;top:52px;width:138px;height:46px;background:var(--green);border-radius:4px;color:var(--white);font:600 14px "Roboto Slab",serif;display:flex;align-items:center;justify-content:space-between;padding:0 12px 0 18px}

/* hero */
.hero{left:0;top:106px;width:1200px;height:620px;background:linear-gradient(90deg,#5a5d5f 0%,#8a8f8c 28%,#4f8a3b 48%,#6aa74a 70%,#3f6e34 100%)}
.hero-shade{left:0;top:106px;width:620px;height:620px;background:linear-gradient(90deg,rgba(40,40,40,.55),rgba(40,40,40,0))}
.hero-title{left:111px;top:268px;font:600 50px "Roboto Slab",serif;color:var(--white);display:flex;gap:10px}
.hero-title span{background:var(--green);padding:0 12px}
.hero-text{left:111px;top:339px;width:380px;font:500 15px/23px "Montserrat",sans-serif;color:var(--white)}
.zip{left:111px;top:401px;width:453px;height:50px;background:var(--white);border-radius:3px;display:flex;align-items:center;justify-content:space-between;padding:0 4px 0 14px}
.zip span{font:400 14px "Roboto Slab",serif;color:#aaa}
.zip b{background:var(--green);color:var(--white);font:600 14px "Roboto Slab",serif;padding:11px 10px;border-radius:2px}
.no-card{left:111px;top:466px;font:400 13px "Roboto Slab",serif;color:var(--white)}
.dots{display:flex;gap:7px}
.dots i{width:9px;height:9px;border-radius:50%;border:1px solid var(--white);display:block}
.dots i.on{background:var(--white)}
.hero-dots{left:111px;top:619px}
.hero-circle{left:1010px;top:559px;width:164px;height:164px;border-radius:50%;border:7px solid var(--white);background:radial-gradient(circle,#6ca94f,#4a8c3a)}
.hero-curve{left:0;top:600px}

/* section titles */
.section-title{font:700 44px "Roboto Slab",serif;color:var(--ink);text-align:center;left:0;width:1200px}
.title-line{height:3px;background:var(--green)}

/* services */
.service{width:473px;height:391px;border-radius:6px;overflow:hidden;box-shadow:0 6px 14px rgba(0,0,0,.2)}
.service-label{position:absolute;left:0;bottom:0;width:100%;height:130px;background:linear-gradient(180deg,rgba(83,168,67,0),var(--green) 75%);display:flex;align-items:flex-end;justify-content:center;padding-bottom:26px;font:500 24px "Oswald",sans-serif;color:var(--white);letter-spacing:.5px;gap:22px}

/* about */
.about-img{left:0;top:1368px;width:584px;height:482px;background:linear-gradient(160deg,#6f8a4a,#a59a86 55%,#8bb35f)}
.about-panel{left:584px;top:1368px;width:616px;height:482px;background:var(--green)}
.about-title{left:616px;top:1435px;font:700 42px "Roboto Slab",serif;color:var(--ink)}
.about-text{left:616px;top:1522px;width:473px;font:400 15px/24.6px "Montserrat",sans-serif;color:var(--white)}
.btn-dark{left:616px;top:1718px;width:140px;height:48px;background:var(--dark);border-radius:5px;color:var(--white);font:600 14px "Roboto Slab",serif;display:flex;align-items:center;justify-content:space-between;padding:0 12px 0 18px}

/* testimonials */
.t-card{top:2017px;width:310px;height:277px;background:var(--white);border-radius:6px;box-shadow:0 3px 12px rgba(0,0,0,.16);text-align:center;padding-top:26px}
.t-name{font:600 18px "Roboto Slab",serif;color:var(--ink)}
.t-role{font:400 11px "Montserrat",sans-serif;color:var(--text);margin-top:2px}
.t-stars{color:var(--star);font-size:15px;letter-spacing:1px;margin-top:6px}
.t-text{font:italic 400 13px/23px "Montserrat",sans-serif;color:var(--text);padding:0 40px;margin-top:14px}
.t-quote{top:2261px;width:82px;height:82px;border-radius:50%;background:var(--green);display:flex;align-items:center;justify-content:center;color:var(--white);font:700 54px/1 "Roboto Slab",serif;padding-top:20px}
.t-dots{left:565px;top:2378px;display:flex;gap:6px}
.t-dots i{width:12px;height:12px;border-radius:50%;background:#777;display:block}
.t-dots i.on{background:var(--green);border:2px solid #555}

/* faq */
.faq{left:111px;top:2477px;width:976px;height:678px;background:var(--green);border-radius:3px}
.faq-item{left:225px;width:748px;height:50px;background:var(--white);border-radius:14px;display:flex;align-items:center;justify-content:space-between;padding:0 36px 0 46px;font:600 14px "Roboto Slab",serif;color:var(--ink);box-shadow:0 2px 6px rgba(0,0,0,.12)}
.faq-item b{font:400 20px "Montserrat",sans-serif}
.faq-open{left:225px;top:2910px;width:748px;height:158px;background:var(--white);border-radius:10px;padding:18px 28px 0 46px;box-shadow:0 2px 6px rgba(0,0,0,.12)}
.faq-open h4{font:600 14px "Roboto Slab",serif;color:var(--ink);display:flex;justify-content:space-between}
.faq-open p{font:400 12.5px/20px "Montserrat",sans-serif;color:var(--text);margin-top:4px;text-align:justify}

/* contact */
.git-title{left:116px;top:3260px;font:700 38px "Roboto Slab",serif;color:var(--ink)}
.map{left:111px;top:3337px;width:476px;height:199px;border-radius:10px;background:linear-gradient(135deg,#e8ebee,#d9dde2);box-shadow:0 2px 8px rgba(0,0,0,.12)}
.info{left:116px;display:flex;gap:24px;align-items:flex-start}
.info-icon{width:40px;height:40px;border-radius:50%;background:var(--dark);display:flex;align-items:center;justify-content:center;flex:none}
.info-text{font:400 15px/22px "Montserrat",sans-serif;color:var(--ink)}
.info-text small{display:block;font-size:14px;color:var(--text)}
.contact-box{left:633px;top:3241px;width:454px;height:649px;background:var(--green);border-radius:14px;box-shadow:0 4px 12px rgba(0,0,0,.18);z-index:3}
.contact-title{left:48px;top:34px;font:700 40px "Roboto Slab",serif;color:var(--ink)}
.contact-note{left:48px;top:124px;width:370px;font:italic 400 11.5px/21px "Montserrat",sans-serif;color:var(--ink)}
.field{left:48px;width:362px;height:42px;background:#050505;border-radius:3px;display:flex;align-items:center;gap:12px;padding:0 14px;font:400 12px "Roboto Slab",serif;color:var(--white)}
.field.tall{height:123px;align-items:flex-start;padding-top:12px}
.captcha{left:53px;top:459px;width:238px;height:60px;background:#f9f9f9;border:1px solid #d3d3d3;border-radius:3px;display:flex;align-items:center;gap:12px;padding:0 12px;font:400 11px "Montserrat",sans-serif;color:#222}
.captcha i{width:22px;height:22px;border:2px solid #c1c1c1;border-radius:2px;background:var(--white);display:block}
.captcha em{margin-left:auto;width:28px;height:28px;background:#9ab0d8;border-radius:50%;display:block}
.send{left:48px;top:533px;width:362px;height:44px;border:2px solid var(--ink);border-radius:3px;display:flex;align-items:center;justify-content:center;font:500 14px "Montserrat",sans-serif;color:var(--ink);letter-spacing:.5px}

/* footer */
.footer-curve{left:0;top:3815px}
.footer{left:0;top:3900px;width:1200px;height:254px;background:var(--dark)}
.f-logo{left:116px;top:3960px;font:700 40px "Roboto Slab",serif;color:var(--white)}
.f-phone{left:302px;top:3958px;font:700 34px "Roboto Condensed",sans-serif;color:var(--white)}
.f-social{left:304px;top:4009px;display:flex;gap:10px}
.f-social i{width:32px;height:32px;border-radius:50%;background:#3a3a40;display:block}
.f-col{top:3928px}
.f-col h5{font:700 15px "Roboto Condensed",sans-serif;color:var(--white);letter-spacing:.5px}
.f-col h5::after{content:"";display:block;width:46px;height:2px;background:var(--green);margin-top:10px}
.f-col ul{list-style:none;margin-top:14px}
.f-col li{font:400 12.5px "Montserrat",sans-serif;color:var(--white);height:26px}
.copy{left:0;top:4154px;width:1200px;height:45px;background:var(--green);display:flex;align-items:center;justify-content:center;font:400 13px "Montserrat",sans-serif;color:var(--ink)}
</style>
</head>
<body>

<!-- header -->
<div class="abs topbar"></div>
<div class="abs topbar-phone">
  <svg width="16" height="16" viewBox="0 0 24 24"><path fill="#1f1f24" d="M6.6 10.8a15 15 0 0 0 6.6 6.6l2.2-2.2c.3-.3.7-.4 1-.2 1.1.4 2.3.6 3.6.6.6 0 1 .4 1 1V20c0 .6-.4 1-1 1A17 17 0 0 1 3 4c0-.6.4-1 1-1h3.5c.6 0 1 .4 1 1 0 1.3.2 2.5.6 3.6.1.3 0 .7-.2 1z"/></svg>
  <small>24/7 Customer Service</small>
  <strong>+1 555 014 2290</strong>
</div>
<div class="abs navbar"></div>
<div class="abs logo-box"><span class="logo-name">Haulwell</span></div>
<nav class="abs nav">
  <span class="active">Home</span><span>What We Do</span><span>What We Take</span><span>Pricing</span><span>Start A Franchise</span>
</nav>
<div class="abs nav-sep"></div>
<svg class="abs search" width="20" height="20" viewBox="0 0 24 24"><circle cx="10" cy="10" r="7" fill="none" stroke="#1f1f24" stroke-width="2.5"/><path d="M15 15l6 6" stroke="#1f1f24" stroke-width="2.5" stroke-linecap="round"/></svg>
<div class="abs btn-contact">Contact Us
  <svg width="20" height="20" viewBox="0 0 20 20"><circle cx="10" cy="10" r="9" fill="#fff"/><path d="M8 6l4 4-4 4" fill="none" stroke="#53a843" stroke-width="2"/></svg>
</div>

<!-- hero -->
<div class="abs hero" role="img" aria-label="Two workers in safety vests lifting a yellow bin into a green garbage truck, with wheelie bins and trees"></div>
<div class="abs hero-shade"></div>
<h1 class="abs hero-title">Junk <span>Removal</span></h1>
<p class="abs hero-text">Saers lksess epiciatis unde omnisiste natuserror sitvolup tatem asccusan tium doloremque.</p>
<div class="abs zip"><span>Enter Your ZIP Code</span><b>Check Availability</b></div>
<p class="abs no-card">No credit card required</p>
<div class="abs dots hero-dots"><i></i><i class="on"></i><i></i><i></i></div>
<svg class="abs hero-curve" width="1200" height="130" viewBox="0 0 1200 130"><path d="M0 44 C220 100 420 135 640 126 C860 118 1050 90 1200 40 L1200 130 L0 130 Z" fill="#fff"/></svg>
<div class="abs hero-circle" role="img" aria-label="Close-up of green grass"></div>

<!-- services -->
<h2 class="abs section-title" style="top:795px">Our Services</h2>
<div class="abs service" style="left:111px;top:895px;background:linear-gradient(160deg,#8a8c88,#5d5a52 50%,#7a7d74)" role="img" aria-label="Worker unloading debris from the back of a commercial truck">
  <div class="service-label">COMMERCIAL <span>+</span></div>
</div>
<div class="abs service" style="left:616px;top:895px;background:linear-gradient(160deg,#c9c9c6,#9a9890 50%,#7f8a6a)" role="img" aria-label="Green dumpster full of boxes and bags outside a residential building">
  <div class="service-label">RESIDENTIAL <span>+</span></div>
</div>

<!-- about -->
<div class="abs about-img" role="img" aria-label="Pile of old timber and rubble beside a green skip near a house"></div>
<div class="abs about-panel"></div>
<h2 class="abs about-title">About Us</h2>
<p class="abs about-text">Saerspiciatis undeasepoiise oklasdo mnis aidaste natus error sit voluptatem accusan tium doloremque laudantium, totam rem aperiam, ease aque ipaefdsa quae ab illo inventore veritatis ease quasi architecto beatae vitae dicta sunt explicabo. Nemo enim ipsam voluptatem quia volasdfupta sde sessitasese aspernatur autodit aut fugitsdsed quisaea consequuntur magni dolores eos qui ratione voluptatem sequi nesciunt.</p>
<div class="abs btn-dark">Learn More
  <svg width="20" height="20" viewBox="0 0 20 20"><circle cx="10" cy="10" r="9" fill="#fff"/><path d="M8 6l4 4-4 4" fill="none" stroke="#242428" stroke-width="2"/></svg>
</div>

<!-- testimonials -->
<h2 class="abs section-title" style="top:1918px">Testimonials</h2>
<div class="abs title-line" style="left:530px;top:1980px;width:140px"></div>

<div class="abs t-card" style="left:111px">
  <div class="t-name">Corwin Telby</div><div class="t-role">Brimlow, CEO</div><div class="t-stars">★★★★★</div>
  <p class="t-text">Saerspiciatis unde omnis iste natus error sitvoluptatem accusan tium doloremque laudantiumotam rem aperiameaque ipaefdsa quae abillo inventore veritatiset.</p>
</div>
<div class="abs t-card" style="left:445px">
  <div class="t-name">Corwin Telby</div><div class="t-role">Brimlow, CEO</div><div class="t-stars">★★★★★</div>
  <p class="t-text">Saerspiciatis unde omnis iste natus error sitvoluptatem accusan tium doloremque laudantiumotam rem aperiameaque ipaefdsa quae abillo inventore veritatiset.</p>
</div>
<div class="abs t-card" style="left:778px">
  <div class="t-name">Corwin Telby</div><div class="t-role">Brimlow, CEO</div><div class="t-stars">★★★★★</div>
  <p class="t-text">Saerspiciatis unde omnis iste natus error sitvoluptatem accusan tium doloremque laudantiumotam rem aperiameaque ipaefdsa quae abillo inventore veritatiset.</p>
</div>
<div class="abs t-quote" style="left:225px">“</div>
<div class="abs t-quote" style="left:559px">“</div>
<div class="abs t-quote" style="left:892px">“</div>
<div class="abs t-dots"><i></i><i class="on"></i><i></i><i></i></div>

<!-- faq -->
<div class="abs faq"></div>
<h2 class="abs section-title" style="top:2540px">Faq</h2>
<div class="abs title-line" style="left:541px;top:2600px;width:127px;background:var(--ink)"></div>
<div class="abs faq-item" style="top:2625px">Perspiciatis unde omnis iste natus errorsit voluptatem <b>+</b></div>
<div class="abs faq-item" style="top:2697px">Hnventore veritatis et quasi architecto beatae vitae dicta sunt explicabo. <b>+</b></div>
<div class="abs faq-item" style="top:2767px">Suia consequuntur magni dolores eos qui ratione voluptatem sequi nesciunt. <b>+</b></div>
<div class="abs faq-item" style="top:2839px">Fautem vel eum iure reprehenderit qui in ea voluptate velit esse quam <b>+</b></div>
<div class="abs faq-open">
  <h4>Lalorem ipsum quia dolor sit amet, consectetur <span>-</span></h4>
  <p>Saerspiciatis undeasepoiise omnis iste natus error sit voluptatem accusan tium doloremque laudantium, totam rem aperiam, ease aque ipaefdsa quae ab illo inventore veritatis ease quasi architecto beatae vitae dicta sunt explicabo. Nemo enim ipsam voluptatem quia volupta sde sessitasese aspernatur autodit aut fugitsdsed quia consequuntur magni dolores eos qui ratione voluptatem sequi nesciunt.</p>
</div>

<!-- get in touch -->
<h2 class="abs git-title">Get In Touch</h2>
<div class="abs map" role="img" aria-label="Street map of the service area with a red location pin"></div>

<div class="abs info" style="top:3570px">
  <div class="info-icon"><svg width="18" height="18" viewBox="0 0 24 24"><path fill="#53a843" d="M12 2a7 7 0 0 0-7 7c0 5 7 13 7 13s7-8 7-13a7 7 0 0 0-7-7zm0 9.5A2.5 2.5 0 1 1 12 6.5a2.5 2.5 0 0 1 0 5z"/></svg></div>
  <div class="info-text"><small>Address</small>42 Larkmere Rd, Dunvale<br>Ashford, Canada, 55210</div>
</div>
<div class="abs info" style="top:3656px">
  <div class="info-icon"><svg width="18" height="18" viewBox="0 0 24 24"><path fill="#53a843" d="M6.6 10.8a15 15 0 0 0 6.6 6.6l2.2-2.2c.3-.3.7-.4 1-.2 1.1.4 2.3.6 3.6.6.6 0 1 .4 1 1V20c0 .6-.4 1-1 1A17 17 0 0 1 3 4c0-.6.4-1 1-1h3.5c.6 0 1 .4 1 1 0 1.3.2 2.5.6 3.6.1.3 0 .7-.2 1z"/></svg></div>
  <div class="info-text"><small>Call Us</small>+1 (555) 014-2290</div>
</div>
<div class="abs info" style="top:3722px">
  <div class="info-icon"><svg width="18" height="18" viewBox="0 0 24 24"><rect x="3" y="5" width="18" height="14" rx="2" fill="#53a843"/><path d="M3 7l9 6 9-6" fill="none" stroke="#242428" stroke-width="1.8"/></svg></div>
  <div class="info-text"><small>Email</small>hello@haulwell.example</div>
</div>

<!-- footer -->
<svg class="abs footer-curve" width="1200" height="90" viewBox="0 0 1200 90"><path d="M0 40 C200 12 420 0 640 10 L1200 60 L1200 90 L0 90 Z" fill="#242428"/></svg>
<div class="abs footer"></div>

<div class="abs contact-box">
  <h2 class="abs contact-title">Contact Us</h2>
  <p class="abs contact-note">Saerspiciatis unde omnis iste natus error sitvoluptatem accusan tium doloremque laudantiumotam.</p>
  <div class="abs field" style="top:173px"><svg width="13" height="13" viewBox="0 0 24 24"><circle cx="12" cy="7" r="5" fill="#fff"/><path d="M3 22c0-5 4-8 9-8s9 3 9 8z" fill="#fff"/></svg>Your Name</div>
  <div class="abs field" style="top:223px"><svg width="14" height="12" viewBox="0 0 24 20"><rect x="1" y="2" width="22" height="16" rx="2" fill="#fff"/><path d="M1 4l11 7 11-7" fill="none" stroke="#050505" stroke-width="2"/></svg>Email</div>
  <div class="abs field" style="top:274px"><svg width="13" height="13" viewBox="0 0 24 24"><path fill="#fff" d="M6.6 10.8a15 15 0 0 0 6.6 6.6l2.2-2.2c.3-.3.7-.4 1-.2 1.1.4 2.3.6 3.6.6.6 0 1 .4 1 1V20c0 .6-.4 1-1 1A17 17 0 0 1 3 4c0-.6.4-1 1-1h3.5c.6 0 1 .4 1 1 0 1.3.2 2.5.6 3.6.1.3 0 .7-.2 1z"/></svg>Phone Number</div>
  <div class="abs field tall" style="top:324px"><svg width="13" height="15" viewBox="0 0 24 24"><path fill="#fff" d="M12 2a7 7 0 0 0-7 7c0 5 7 13 7 13s7-8 7-13a7 7 0 0 0-7-7zm0 9.5A2.5 2.5 0 1 1 12 6.5a2.5 2.5 0 0 1 0 5z"/></svg>Address</div>
  <div class="abs captcha"><i></i>I'm not a robot<em></em></div>
  <div class="abs send">SEND MESSAGE</div>
</div>

<div class="abs f-logo">Haulwell</div>
<div class="abs f-phone">+1 555 014 2290</div>
<div class="abs f-social"><i></i><i></i><i></i></div>

<div class="abs f-col" style="left:637px"><h5>QUICK LINKS</h5>
  <ul><li>HOME</li><li>WHAT WE DO</li><li>WHAT WE TAKE</li><li>PRICING</li><li>START A FRANCHISE</li><li>CONTACT US</li></ul></div>
<div class="abs f-col" style="left:827px"><h5>LINKS</h5>
  <ul><li>COPYRIGHT</li><li>LEGAL</li><li>PRIVACY</li><li>ACCESSIBILITY</li><li>SITEMAP</li></ul></div>
<div class="abs f-col" style="left:988px"><h5>SUPPORT</h5>
  <ul><li>TEAM</li><li>ABOUT US</li><li>CAREERS</li><li>OUR VALUES</li></ul></div>

<div class="abs copy">©2023. All rights reserved.</div>

</body>
</html>
```